Investment firm needs refreshed corporate powerpoint slides design

We need a new and refreshed powerpoint template for our corporate investment deck. We are a technology private equity group that primarily invests in fast growing software companies and we would like to reflect that in a modern and light blue / transparant / white powerpoint and fonts template. I have also attached our old investor deck as a guideline and also check out our website to get an idea of what we do and what type of companies we invested in. Please note that our website is old and so our presentation should be a refreshed "2017" modern design, not a copy / paste of our website design and graphics.
Updates

Project Deadline Extended Reason: I'm extending the deadline to February 27, but we would ideally receive something by the end of this week.Please submit updates. Thanks Added Tuesday, February 21, 2017

Target Market(s)

Investors such as high net worth individuals, pension funds, banks, financial advisors

Industry/Entity Type

Investment

Colors
33a6d7
85cae6
cfeae6
edf8f6
ffffff
fff3d1
86cfc6

Requirements
Must have
• We let you be creative, we trust you have seen more investment presentations before.
Nice to have
• Pre-built models, flow charts, graphs, charts, etc.
Should not have
• Fancy or edgy images, this has to be a modern, fresh and trustworthy looking powerpoint template. No stock images, if you do use stock images for background purposes please be creative! :-)

```html
<!DOCTYPE html>
<html lang="en">
<head>
<meta charset="utf-8">
<title>Corporate Deck Template</title>
<link href="https://fonts.googleapis.com/css2?family=Open+Sans:wght@400;600;700&display=swap" rel="stylesheet">
<style>
  :root {
    --page-bg: #ececea;
    --white: #ffffff;
    --navy: #0f2a5c;
    --navy-deep: #0a2453;
    --blue: #1f8fd0;
    --blue-light: #33a6d7;
    --teal: #86cfc6;
    --mint: #cfeae6;
    --ice: #d9edf4;
    --text: #2c2f36;
    --muted: #7a7f88;
    --arrow: #8a8f96;
  }
  * { box-sizing: border-box; margin: 0; padding: 0; }
  html, body { width: 1200px; height: 2799px; overflow: hidden; }
  body {
    background: var(--page-bg);
    font-family: "Open Sans", Arial, sans-serif;
    color: var(--text);
    position: relative;
  }
  .slide {
    position: absolute;
    left: 88px;
    width: 1026px;
    height: 577px;
    background: var(--white);
    box-shadow: 0 2px 5px rgba(0,0,0,0.35);
    overflow: hidden;
  }
  .slide--banner { top: 69px; }
  .slide--sidebar { top: 683px; }
  .slide--band { top: 1297px; }

  .title { position: absolute; font-weight: 400; white-space: nowrap; }
  .subtitle { position: absolute; font-size: 13px; white-space: nowrap; }

  .column { position: absolute; width: 440px; }
  .column h2 {
    font-size: 25px;
    line-height: 32px;
    font-weight: 400;
    display: flex;
    align-items: center;
    gap: 10px;
    white-space: nowrap;
  }
  .column h2::before {
    content: "";
    width: 0; height: 0;
    border-top: 9px solid transparent;
    border-bottom: 9px solid transparent;
    border-left: 10px solid var(--arrow);
  }
  .column ul {
    list-style: none;
    margin: 6px 0 0 34px;
    width: 400px;
  }
  .column li {
    position: relative;
    font-size: 15px;
    line-height: 20px;
    margin-bottom: 14px;
    padding-left: 24px;
    white-space: nowrap;
  }
  .column li::before {
    content: "";
    position: absolute;
    left: 2px; top: 8px;
    width: 5px; height: 5px;
    border-radius: 50%;
    background: currentColor;
  }

  .brand {
    position: absolute;
    display: flex;
    align-items: center;
    gap: 10px;
    font-size: 34px;
    line-height: 40px;
    font-weight: 400;
    color: var(--navy);
    letter-spacing: -0.5px;
  }
  .brand__mark { width: 9px; height: 9px; background: var(--arrow); }
  .page-num { position: absolute; font-size: 12px; color: var(--muted); }

  /* Slide 1 */
  .slide--banner .header {
    position: absolute; left: 0; top: 0; width: 100%; height: 110px;
    background: linear-gradient(90deg, var(--navy-deep) 0%, #2b5d80 35%, #7cc9b6 62%, var(--ice) 88%, #e6f3f8 100%);
    border-bottom: 3px solid #c9d3dc;
  }
  .slide--banner .title { left: 65px; top: 20px; font-size: 33px; color: var(--white); }
  .slide--banner .subtitle { left: 68px; top: 66px; color: var(--white); }
  .slide--banner .column h2 { color: var(--navy); font-weight: 700; }
  .slide--banner .col-left { left: 84px; top: 156px; }
  .slide--banner .col-right { left: 568px; top: 156px; }
  .slide--banner .brand { left: 43px; top: 505px; }
  .slide--banner .page-num { left: 959px; top: 528px; }

  /* Slide 2 */
  .slide--sidebar .sidebar {
    position: absolute; left: 0; top: 0; width: 101px; height: 100%;
    background: linear-gradient(180deg, var(--white) 0%, #cfe6f3 18%, #3a97cf 42%, #1d5a97 62%, var(--navy-deep) 100%);
    border-right: 3px solid #c9d3dc;
  }
  .slide--sidebar .title { left: 124px; top: 22px; font-size: 42px; color: var(--navy); }
  .slide--sidebar .subtitle { left: 127px; top: 76px; color: var(--muted); }
  .slide--sidebar .column h2 { color: var(--blue); }
  .slide--sidebar .col-left { left: 130px; top: 157px; }
  .slide--sidebar .col-right { left: 565px; top: 157px; }
  .slide--sidebar .brand { left: 824px; top: 512px; }
  .slide--sidebar .page-num { left: 127px; top: 533px; }

  /* Slide 3 */
  .slide--band .title { left: 61px; top: 16px; font-size: 33px; color: var(--blue); }
  .slide--band .subtitle { left: 62px; top: 68px; color: var(--muted); }
  .slide--band .band {
    position: absolute; left: 0; top: 106px; width: 100%; height: 405px;
    background: linear-gradient(100deg, #2d95d0 0%, #2178b7 35%, #14477f 70%, var(--navy-deep) 100%);
  }
  .slide--band .column { color: var(--white); }
  .slide--band .column h2 { color: var(--white); }
  .slide--band .column h2::before { display: none; }
  .slide--band .column ul { margin-left: 20px; }
  .slide--band .col-left { left: 112px; top: 155px; }
  .slide--band .col-right { left: 546px; top: 155px; }
  .slide--band .brand { left: 824px; top: 527px; }
  .slide--band .page-num { left: 71px; top: 544px; }
</style>
</head>
<body>

<section class="slide slide--banner">
  <div class="header"></div>
  <h1 class="title">Lorem ipsum dolor sit amet</h1>
  <p class="subtitle">Lorem ipsum dolor sit amet, consetetur sadipscing elitr</p>
  <div class="column col-left">
    <h2>Investment Prospect</h2>
    <ul>
      <li>Custom built algorithms developed over 7<br>years</li>
      <li>Screen 100K companies every 8 weeks</li>
      <li>Revenue size, revenue growth, funding,<br>social connections,<br>and themes</li>
      <li>Senior level outreach to prospects through<br>social network contacts</li>
      <li>Sourcing efficiencies in team size and<br>processing time</li>
    </ul>
  </div>
  <div class="column col-right">
    <h2>Executive Identification</h2>
    <ul>
      <li>HV Growth’s executive advisory board</li>
      <li>Screen 15 years of M&amp;A history</li>
      <li>High value, capital-efficient exits, geography,<br>market segment</li>
      <li>Establish connections early with deal pipeline</li>
      <li>Differentiates HV Growth in competitive<br>processes</li>
    </ul>
  </div>
  <div class="brand"><span class="brand__mark"></span>Halvard</div>
  <span class="page-num">5</span>
</section>

<section class="slide slide--sidebar">
  <div class="sidebar"></div>
  <h1 class="title">Lorem ipsum dolor sit amet</h1>
  <p class="subtitle">Lorem ipsum dolor sit amet, consetetur sadipscing elitr</p>
  <div class="column col-left">
    <h2>Investment Prospect</h2>
    <ul>
      <li>Custom built algorithms developed over 7<br>years</li>
      <li>Screen 100K companies every 8 weeks</li>
      <li>Revenue size, revenue growth, funding,<br>social connections,<br>and themes</li>
      <li>Senior level outreach to prospects through<br>social network contacts</li>
      <li>Sourcing efficiencies in team size and<br>processing time</li>
    </ul>
  </div>
  <div class="column col-right">
    <h2>Executive Identification</h2>
    <ul>
      <li>HV Growth’s executive advisory board</li>
      <li>Screen 15 years of M&amp;A history</li>
      <li>High value, capital-efficient exits, geography,<br>market segment</li>
      <li>Establish connections early with deal pipeline</li>
      <li>Differentiates HV Growth in competitive<br>processes</li>
    </ul>
  </div>
  <span class="page-num">6</span>
  <div class="brand"><span class="brand__mark"></span>Halvard</div>
</section>

<section class="slide slide--band">
  <h1 class="title">Lorem ipsum dolor sit amet</h1>
  <p class="subtitle">Lorem ipsum dolor sit amet, consetetur sadipscing elitr</p>
  <div class="band"></div>
  <div class="column col-left">
    <h2>Investment Prospect</h2>
    <ul>
      <li>Custom built algorithms developed over 7<br>years</li>
      <li>Screen 100K companies every 8 weeks</li>
      <li>Revenue size, revenue growth, funding,<br>social connections,<br>and themes</li>
      <li>Senior level outreach to prospects through<br>social network contacts</li>
      <li>Sourcing efficiencies in team size and<br>processing time</li>
    </ul>
  </div>
  <div class="column col-right">
    <h2>Executive Identification</h2>
    <ul>
      <li>HV Growth’s executive advisory board</li>
      <li>Screen 15 years of M&amp;A history</li>
      <li>High value, capital-efficient exits, geography,<br>market segment</li>
      <li>Establish connections early with deal pipeline</li>
      <li>Differentiates HV Growth in competitive<br>processes</li>
    </ul>
  </div>
  <span class="page-num">6</span>
  <div class="brand"><span class="brand__mark"></span>Halvard</div>
</section>

</body>
</html>
```